Marlowe's Classic Dressing

We are looking for a new label as we switch or glass bottle from a traditional bottle to a round bottle. We want to create a newer/ more appealing logo, while still maintaining some of our old label features to ensure that the brand awareness is not lost. We like the coloring of the blue and white, but feel free to play around with other colors in the design.
We are looking to add product features to our label such as "Gluten-Free", "Original Recipe From 1957" "Family Owned". With this being an older company we would like to keep the traditional feel of our label with some added modern touches.
We are not married to the greek logo/ building but would love some designs with and without it.
WE ARE LOOKING FOR A ROUND LABEL. The pictures provided below are of the old bottle.
There is a picture of the ringneck bottle below. The size of the label is 4.00 x 7.00.

```html
<!DOCTYPE html>
<html lang="en">
<head>
<meta charset="utf-8">
<title>Marlowe's Classic Dressing – Label</title>
<link rel="stylesheet" href="https://fonts.googleapis.com/css2?family=Oswald:wght@600;700&family=Courier+Prime:wght@400;700&display=swap">
<style>
  :root {
    --page-bg: #ffffff;
    --label-blue-light: #8fa8c4;
    --label-blue: #6786ab;
    --label-blue-deep: #4f6f95;
    --band-dark: #363f4c;
    --ink-white: #f2f2f0;
    --ink-soft: #e3e8ee;
    --temple-dark: #27303d;
    --trim-grey: #cfd3d8;
  }
  html, body {
    margin: 0;
    padding: 0;
    width: 1200px;
    height: 1200px;
    overflow: hidden;
    background: var(--page-bg);
  }
  .canvas {
    width: 1200px;
    height: 1200px;
    display: flex;
    align-items: center;
    justify-content: center;
  }
  .label { display: block; }
  .brand-name {
    font-family: "Oswald", sans-serif;
    font-weight: 600;
    fill: var(--ink-white);
  }
  .band-text, .recipe-line, .claims, .volume {
    font-family: "Courier Prime", monospace;
    fill: var(--ink-soft);
  }
  .band-text { font-size: 19px; letter-spacing: 2px; }
  .recipe-line { font-size: 17px; }
  .claims { font-size: 17px; letter-spacing: 1.5px; font-weight: 700; }
  .volume { font-size: 15px; letter-spacing: 1px; }
  .product-type {
    font-family: "Oswald", sans-serif;
    font-weight: 700;
    fill: var(--ink-white);
  }
</style>
</head>
<body>
<main class="canvas">
  <svg class="label" width="589" height="995" viewBox="0 0 512 865" xmlns="http://www.w3.org/2000/svg" aria-label="Marlowe's Greek Dressing label">
    <defs>
      <linearGradient id="label-fill" x1="0" y1="0" x2="1" y2="0">
        <stop offset="0" stop-color="var(--label-blue-light)"/>
        <stop offset="0.45" stop-color="var(--label-blue)"/>
        <stop offset="1" stop-color="var(--label-blue-deep)"/>
      </linearGradient>
    </defs>

    <rect class="label-body" x="0" y="0" width="512" height="845" fill="url(#label-fill)"/>
    <rect class="label-trim" x="0" y="845" width="512" height="20" fill="var(--trim-grey)"/>

    <text class="brand-name" x="256" y="168" font-size="74" text-anchor="middle">Marlowe's</text>

    <rect class="temple-artwork" role="img" aria-label="Illustration of a classical Greek temple" x="140" y="228" width="224" height="98" fill="var(--temple-dark)" opacity="0.55"/>

    <rect class="feature-band" x="78" y="327" width="365" height="60" fill="var(--band-dark)"/>
    <text class="band-text" x="260" y="364" text-anchor="middle">· FAMILY OWNED ·</text>

    <text class="product-type" x="256" y="530" font-size="128" text-anchor="middle" letter-spacing="4">GREEK</text>
    <text class="product-type" x="256" y="608" font-size="60" text-anchor="middle" letter-spacing="2">DRESSING</text>

    <text class="recipe-line" x="256" y="672" text-anchor="middle">- Original Recipe From 1957 -</text>
    <line class="divider" x1="73" y1="700" x2="448" y2="700" stroke="var(--ink-soft)" stroke-width="1" opacity="0.7"/>
    <text class="claims" x="256" y="742" text-anchor="middle">·GLUTEN FREE·NON GMO·</text>
    <line class="divider-short" x1="158" y1="770" x2="358" y2="770" stroke="var(--band-dark)" stroke-width="3"/>
    <text class="volume" x="256" y="806" text-anchor="middle">8 Fl Oz (237ml)</text>
  </svg>
</main>
</body>
</html>
```